Business card design needed

We do excavation, cartage and contracting
I would quote like to have a picture of my digger as the whole back ground and the words on top. If that looks any good
Otherwise please feel free to come up with any other cool options

Cheers Marc

KLR Contracting
Excavation, Cartage, Contracting
Marcus Prewitt
www.klr-example.co.nz
021 584 067
marc@klr-example.co.nz

```html
<!DOCTYPE html>
<html lang="en">
<head>
<meta charset="utf-8">
<title>KLR Contracting – Business Card</title>
<link rel="stylesheet" href="https://fonts.googleapis.com/css2?family=Source+Sans+3:wght@400;600;700&display=swap">
<style>
  :root {
    --card-bg: #ebebea;
    --digger-tone: #e2e2e0;
    --brand-green: #1f5a2c;
    --contact-grey: #5a5a5a;
  }
  * { margin: 0; padding: 0; box-sizing: border-box; }
  html, body {
    width: 1200px;
    height: 765px;
    overflow: hidden;
    background: var(--card-bg);
  }
  .card {
    position: relative;
    width: 1200px;
    height: 765px;
    background: var(--card-bg);
    font-family: "Source Sans 3", "Myriad Pro", Arial, sans-serif;
    overflow: hidden;
  }
  .digger-backdrop {
    position: absolute;
    left: 0;
    top: 0;
    width: 1200px;
    height: 765px;
  }
  .contact {
    position: absolute;
    right: 78px;
    top: 62px;
    text-align: right;
  }
  .contact__name {
    font-size: 38px;
    font-weight: 700;
    letter-spacing: 3px;
    color: var(--brand-green);
    line-height: 1;
  }
  .contact__line {
    display: flex;
    justify-content: flex-end;
    align-items: center;
    gap: 10px;
    margin-top: 16px;
    font-size: 24px;
    letter-spacing: 2.5px;
    color: var(--contact-grey);
    line-height: 1;
  }
  .contact__line svg { flex: none; }
  .brand {
    position: absolute;
    left: 60px;
    top: 270px;
    width: 620px;
    text-align: center;
  }
  .brand__name {
    font-size: 120px;
    font-weight: 600;
    letter-spacing: 6px;
    color: var(--brand-green);
    line-height: 1;
  }
  .brand__services {
    margin-top: 58px;
    font-size: 30px;
    font-weight: 400;
    color: var(--brand-green);
    line-height: 1;
    white-space: nowrap;
  }
  .brand__web {
    margin-top: 12px;
    font-size: 25px;
    letter-spacing: 5px;
    color: var(--brand-green);
    line-height: 1;
  }
</style>
</head>
<body>
  <main class="card">
    <svg class="digger-backdrop" viewBox="0 0 1200 765" role="img" aria-label="Faint outline drawing of an excavator arm and bucket across the card background">
      <polygon points="0,150 490,20 620,90 880,480 860,600 600,690 420,700 240,640 0,590" fill="var(--digger-tone)"/>
    </svg>

    <section class="contact">
      <h1 class="contact__name">Marcus Prewitt</h1>
      <p class="contact__line">
        <svg width="32" height="22" viewBox="0 0 32 22" aria-hidden="true">
          <rect x="1" y="1" width="30" height="20" fill="none" stroke="#5a5a5a" stroke-width="2"/>
          <polyline points="1,1 16,13 31,1" fill="none" stroke="#5a5a5a" stroke-width="2"/>
        </svg>
        marc@klr-example.co.nz
      </p>
      <p class="contact__line">
        <svg width="40" height="40" viewBox="0 0 40 40" aria-hidden="true">
          <circle cx="20" cy="20" r="19" fill="#1f5a2c"/>
          <rect x="12" y="9" width="16" height="22" rx="2" fill="none" stroke="#ffffff" stroke-width="2.5"/>
          <rect x="15" y="13" width="10" height="6" fill="#ffffff"/>
        </svg>
        021 584 067
      </p>
    </section>

    <section class="brand">
      <p class="brand__name">KLR</p>
      <p class="brand__services">Contracting Excavation . Cartage .&nbsp; Contracting</p>
      <p class="brand__web">www.klr-example.co.nz</p>
    </section>
  </main>
</body>
</html>
```